Copper Meadow - responsive bootstrap website design

Looking to build a responsive service website.

Logo has been provided.

PLEASE REVIEW ATTACHED DESIGN STYLE GUIDES & CLIENT CREATIVE BRIEF FOR OUR REQUIREMENT.

THANK YOU AND GOOD LUCK!

Industry/Entity Type

Build

```html
<!DOCTYPE html>
<html lang="en">
<head>
<meta charset="utf-8">
<title>Copper Meadow Outfitters</title>
<link rel="stylesheet" href="https://fonts.googleapis.com/css2?family=Arimo:wght@400;700&display=swap">
<style>
:root{
  --ink:#111;
  --black:#000;
  --bar:#1c1c1c;
  --white:#fff;
  --sky:#3b79c4;
  --text:#6a6a6a;
  --footer-text:#cfcfcf;
  --rule:#b9b9b9;
  --brand-grey:#555;
}
*{margin:0;padding:0;box-sizing:border-box}
html,body{width:1007px;height:1200px;overflow:hidden;background:var(--white);font-family:"Arimo",Arial,sans-serif;color:var(--ink)}
.page{position:relative;width:1007px;height:1200px}
.site-header{position:absolute;left:0;top:0;width:1007px;height:107px;background:var(--black);border-top:9px solid #1a1a1a}
.brand{position:absolute;left:22px;top:22px;color:var(--white);font-size:20px;line-height:25px;text-align:center;width:172px}
.location{position:absolute;left:352px;top:24px;color:var(--sky);font-size:20px;letter-spacing:.4px}
.main-nav{position:absolute;top:64px;left:0;width:1007px;height:14px}
.main-nav a{position:absolute;color:var(--white);text-decoration:none;font-size:10px;letter-spacing:.3px;white-space:nowrap}
.hero{position:absolute;left:0;top:107px;width:1007px;height:332px;
  background:
    radial-gradient(ellipse 300px 110px at 520px 210px,rgba(225,228,232,.75),rgba(225,228,232,0) 70%),
    radial-gradient(ellipse 70px 60px at 505px 40px,rgba(190,160,130,.55),rgba(190,160,130,0) 75%),
    linear-gradient(180deg,#31466a 0%,#3d5478 40%,#2c3f5e 75%,#1f2e47 100%)}
.hero-band{position:absolute;left:168px;top:233px;width:747px;height:62px;background:linear-gradient(90deg,rgba(20,55,110,0) 0%,rgba(20,55,110,.85) 18%,rgba(20,55,110,.85) 82%,rgba(20,55,110,0) 100%)}
.hero-title{position:absolute;left:0;top:244px;width:1007px;text-align:center;color:var(--white);font-size:34px;font-weight:400;letter-spacing:.5px}
.hero-dots{position:absolute;left:4px;top:317px;display:flex;gap:14px}
.hero-dots span{width:8px;height:8px;background:#ddd;opacity:.85}
.shop-bar{position:absolute;left:0;top:439px;width:1007px;height:67px;background:repeating-linear-gradient(135deg,#1e1e1e 0 2px,#262626 2px 4px)}
.shop-bar svg{position:absolute;left:285px;top:12px}
.shop-label{position:absolute;left:353px;top:21px;color:var(--white);font-size:20px}
.shadow-curve{position:absolute;left:200px;top:506px;width:607px;height:14px;background:radial-gradient(ellipse at 50% 0,rgba(0,0,0,.18),rgba(0,0,0,0) 70%)}
.welcome-title{position:absolute;left:0;top:543px;width:1007px;text-align:center;font-size:28px;font-weight:400}
.welcome-text{position:absolute;left:141px;top:602px;width:725px;text-align:center;font-size:16px;line-height:20px;color:var(--text)}
.features{position:absolute;left:0;top:668px;width:1007px;height:255px}
.feature-label{position:absolute;top:38px;color:var(--white);font-size:13px;letter-spacing:1px;transform:translateX(-50%);white-space:nowrap}
.merch-title{position:absolute;left:0;top:954px;width:1007px;text-align:center;font-size:23px;font-weight:400}
.merch-rule{position:absolute;left:284px;top:990px;width:475px;height:1px;background:var(--rule)}
.brands{position:absolute;left:0;top:1043px;width:1007px;height:30px}
.brands span{position:absolute;transform:translateX(-50%);color:var(--brand-grey);font-size:21px;font-weight:700;white-space:nowrap}
.site-footer{position:absolute;left:0;top:1127px;width:1007px;height:73px;background:var(--bar);text-align:center;color:var(--footer-text);font-size:9px;letter-spacing:.6px;line-height:14px;padding-top:19px}
</style>
</head>
<body>
<div class="page">
  <header class="site-header">
    <div class="brand">Copper Meadow<br>Outfitters</div>
    <div class="location">Marsh Point South Carolina</div>
    <nav class="main-nav">
      <a style="left:352px" href="#">HOME PAGE</a>
      <a style="left:459px" href="#">ABOUT US</a>
      <a style="left:559px" href="#">GUIDE SERVICES</a>
      <a style="left:690px" href="#">MERCHANDISE</a>
      <a style="left:810px" href="#">VIDEO</a>
      <a style="left:889px" href="#">PICTURE GALLERY</a>
    </nav>
  </header>

  <section class="hero" role="img" aria-label="Angler on open water holding a large silver amberjack">
    <div class="hero-band"></div>
    <div class="hero-title">COPPER MEADOW OUTFITTERS</div>
    <div class="hero-dots"><span></span><span></span><span></span><span></span></div>
  </section>

  <div class="shop-bar">
    <svg width="52" height="44" viewBox="0 0 52 44" fill="none" stroke="#9a9a9a" stroke-width="2">
      <path d="M2 4h8l7 26h26l6-18H13"/>
      <path d="M16 14h30M18 20h26M20 26h22M24 12v18M32 12v18M40 12v18"/>
      <circle cx="21" cy="38" r="3"/><circle cx="39" cy="38" r="3"/>
    </svg>
    <div class="shop-label">Shop Copper Meadow Outfitters Store</div>
  </div>
  <div class="shadow-curve"></div>

  <h1 class="welcome-title">Welcome to Copper Meadow Outfitters</h1>
  <p class="welcome-text">Lowcountry’s own Copper Meadow Outfitters is your ultimate destination for saltwater fishing. From fly fishing for tailing reds in a foot of water to chasing Pelagic in the Gulf Stream, here you’ll find all the gear, apparel, and expert advice you’ll need to make the most of your time on the water.</p>

  <section class="features">
    <svg width="1007" height="255" viewBox="0 0 1007 255" role="img" aria-label="Faded photo of anglers on the beach">
      <defs>
        <linearGradient id="bandFill" x1="0" y1="0" x2="0" y2="1">
          <stop offset="0" stop-color="#8a9bb0"/>
          <stop offset=".5" stop-color="#7d8fa6"/>
          <stop offset="1" stop-color="#8797ab"/>
        </linearGradient>
        <radialGradient id="guideFill" cx=".5" cy=".45" r=".6"><stop offset="0" stop-color="#c9a184"/><stop offset=".55" stop-color="#8d8a80"/><stop offset="1" stop-color="#b9c6cf"/></radialGradient>
        <linearGradient id="aboutFill" x1="0" y1="0" x2="0" y2="1"><stop offset="0" stop-color="#6f7466"/><stop offset=".6" stop-color="#5a4e40"/><stop offset="1" stop-color="#c9c7c0"/></linearGradient>
        <linearGradient id="merchFill" x1="0" y1="0" x2="1" y2="1"><stop offset="0" stop-color="#cba488"/><stop offset=".55" stop-color="#2e2c2e"/><stop offset="1" stop-color="#9aa7b4"/></linearGradient>
        <linearGradient id="galleryFill" x1="0" y1="0" x2="0" y2="1"><stop offset="0" stop-color="#7fb6e0"/><stop offset=".45" stop-color="#e6ecef"/><stop offset=".75" stop-color="#b8c24a"/><stop offset="1" stop-color="#3e8f6a"/></linearGradient>
      </defs>
      <path d="M0 0 Q503 40 1007 0 V255 Q503 215 0 255 Z" fill="url(#bandFill)"/>
      <path d="M0 0 Q503 40 1007 0 V10 Q503 50 0 10 Z" fill="#6a7e97" opacity=".6"/>
      <circle cx="130" cy="143" r="72" fill="url(#guideFill)" stroke="#fff" stroke-width="2.5" role="img" aria-label="Fishing guide portrait on the marsh"/>
      <circle cx="379" cy="143" r="72" fill="url(#aboutFill)" stroke="#fff" stroke-width="2.5" role="img" aria-label="Catch hanging at the dock"/>
      <circle cx="623" cy="143" r="72" fill="url(#merchFill)" stroke="#fff" stroke-width="2.5" role="img" aria-label="Two divers on a boat"/>
      <circle cx="865" cy="143" r="72" fill="url(#galleryFill)" stroke="#fff" stroke-width="2.5" role="img" aria-label="Angler holding a mahi-mahi"/>
    </svg>
    <span class="feature-label" style="left:132px;font-weight:700">GUIDE SERVICES</span>
    <span class="feature-label" style="left:385px">ABOUT</span>
    <span class="feature-label" style="left:623px">MERCHANDISE</span>
    <span class="feature-label" style="left:867px">PICTURE GALLERY</span>
  </section>

  <h2 class="merch-title">Merchandise at Copper Meadow Outfitters</h2>
  <div class="merch-rule"></div>

  <div class="brands">
    <span style="left:95px">TIDEMARK</span>
    <span style="left:258px">REELHAUS</span>
    <span style="left:463px">Northfork Apparel</span>
    <span style="left:711px">GLINTLINE</span>
    <span style="left:917px">Brine Co.</span>
  </div>

  <footer class="site-footer">
    Site Copyright © 2014 Copper Meadow Outfitters. &nbsp;| &nbsp;www.coppermeadowoutfitters.com<br>
    Please e-mail us if you have any questions or comments about this site.
  </footer>
</div>
</body>
</html>
```